Brand design for Varundel Partners

We are a new start up Fund Manager based in Singapore in need of a stylish and slick corporate identity starting with letterhead and business card (2 separate projects on craft hive but must be completed as one). We are aiming to be a somewhat 'budget' service provider with a target market of high net worth individuals and savvy self traders so we need to have our look convey value but with style. Our logo is attached and the use of the blue is imperative. The company name is Varundel Partners Pte Ltd and the verbiage 'Licensed by the Financial Oversight Board of Singapore - RFMC licence no. QRT804217-3' should be incorporated in small print.

Business card should also include address, office, direct and mobile numbers as well as email address. Follow me on twitter/fb/linkedin/Google+ should also be incrorporated. We are also looking to have a QR code on the business card that people can read with a smartphone which will auto populate our contact details in to their address book.

Many thanks and happy designing!

Reason: Extending so we can have further internal discussions. Thanks for input so far, some great designs coming through! Cheers

```html
<!DOCTYPE html>
<html lang="en">
<head>
<meta charset="utf-8">
<title>Varundel Partners – Letterhead</title>
<link href="https://fonts.googleapis.com/css2?family=Open+Sans:wght@400;600&display=swap" rel="stylesheet">
<style>
  :root {
    --brand-blue: #0a55a6;
    --paper: #ffffff;
    --backdrop: #e4e4e4;
    --band-text: #ffffff;
    --watermark: #e6e6e6;
  }
  * { box-sizing: border-box; margin: 0; padding: 0; }
  html, body {
    width: 1009px;
    height: 1200px;
    overflow: hidden;
    background: var(--backdrop);
    font-family: "Open Sans", Arial, sans-serif;
  }
  .letterhead {
    position: absolute;
    left: 96px;
    top: 13px;
    width: 816px;
    height: 1174px;
    background: var(--paper);
    box-shadow: 0 2px 10px rgba(0,0,0,0.18);
    overflow: hidden;
  }
  .brand-lockup {
    position: absolute;
    top: 44px;
    left: 0;
    width: 100%;
    display: flex;
    justify-content: center;
    align-items: center;
    gap: 16px;
    color: var(--brand-blue);
  }
  .brand-mark {
    width: 40px;
    height: 40px;
    border-radius: 50%;
    background: var(--brand-blue);
  }
  .brand-name {
    font-size: 50px;
    font-weight: 600;
    letter-spacing: 0.5px;
    line-height: 1.2;
  }
  .brand-watermark {
    position: absolute;
    right: 34px;
    top: 640px;
    text-align: right;
    font-size: 118px;
    font-weight: 600;
    line-height: 1.15;
    color: var(--watermark);
    letter-spacing: -1px;
    user-select: none;
  }
  .contact-band {
    position: absolute;
    left: 0;
    top: 1073px;
    width: 100%;
    height: 48px;
    background: var(--brand-blue);
    color: var(--band-text);
  }
  .company-name {
    position: absolute;
    left: 30px;
    top: 11px;
    font-size: 21px;
  }
  .postal-address {
    position: absolute;
    left: 329px;
    top: 3px;
    font-size: 17px;
    line-height: 21px;
    font-style: normal;
  }
  .direct-lines {
    position: absolute;
    left: 593px;
    top: 3px;
    font-size: 17px;
    line-height: 21px;
    list-style: none;
  }
  .direct-lines li { display: flex; align-items: center; gap: 8px; }
  .direct-lines svg { width: 13px; height: 13px; fill: var(--band-text); }
  .licence-note {
    position: absolute;
    left: 0;
    top: 1132px;
    width: 100%;
    text-align: center;
    font-size: 13px;
    color: var(--brand-blue);
  }
</style>
</head>
<body>
  <main class="letterhead">
    <header class="brand-lockup">
      <span class="brand-mark" aria-hidden="true"></span>
      <span class="brand-name">Varundel Partners</span>
    </header>

    <div class="brand-watermark" aria-hidden="true">Varundel<br>Partners</div>

    <footer>
      <div class="contact-band">
        <div class="company-name">Varundel Partners Pte Ltd</div>
        <address class="postal-address">42 Harlow Quay Rd<br>Singapore 248915</address>
        <ul class="direct-lines">
          <li>
            <svg viewBox="0 0 24 24" aria-hidden="true"><path d="M6.6 10.8a15.1 15.1 0 0 0 6.6 6.6l2.2-2.2c.3-.3.7-.4 1-.2 1.1.4 2.3.6 3.6.6.6 0 1 .4 1 1V20c0 .6-.4 1-1 1A17 17 0 0 1 3 4c0-.6.4-1 1-1h3.5c.6 0 1 .4 1 1 0 1.3.2 2.5.6 3.6.1.3 0 .7-.2 1z"/></svg>
            <span>+65 0000 4182</span>
          </li>
          <li>
            <svg viewBox="0 0 24 24" aria-hidden="true"><path d="M2 9l10-6 10 6v11H2z M4 9.6l8 5 8-5-8-4.8z"/></svg>
            <span>contact@varundel.com</span>
          </li>
        </ul>
      </div>
      <p class="licence-note">Licensed by the Financial Oversight Board of Singapore - RFMC licence no. QRT804217-3</p>
    </footer>
  </main>
</body>
</html>
```